Real Estate Webpage Design

We have an existing website: verindaleestates.com.au
We focus customised service mainly on Property Management and second-hand property sales.
We are not entirely happy about the current design and layout can stay roughly the same as the back end coding is linked to a CRM system.
We would like to see the design are more reachable to our clients and appearing.
Please check our Website Design Draft for more details.

Industry/Entity Type

Real estate Agency

Number of Pages Required

5+ page

Font styles to use
Sans Serif

Colors

Designer to choose colors to be used in the design.

```html
<!DOCTYPE html>
<html lang="en">
<head>
<meta charset="utf-8">
<title>Verindale Property Group</title>
<link rel="stylesheet" href="https://fonts.googleapis.com/css2?family=Inter:wght@400;500;600;700&family=Montserrat:wght@700;800&display=swap">
<style>
:root{
  --navy:#0f2a44;
  --navy-deep:#0c2439;
  --gold:#f5b841;
  --band:#fbc862;
  --ink:#1a2433;
  --muted:#8a8f96;
  --line:#e3e3e3;
  --white:#ffffff;
}
*{margin:0;padding:0;box-sizing:border-box}
html,body{width:1200px;height:3084px;overflow:hidden}
body{position:relative;background:var(--white);font-family:"Inter",Arial,sans-serif;color:var(--ink)}

/* header */
.site-header{position:absolute;left:0;top:0;width:1200px;height:80px;background:var(--white)}
.brand{position:absolute;left:110px;top:22px;display:flex;align-items:center;gap:10px}
.brand-mark{width:36px;height:36px;background:var(--gold)}
.brand-name{font-size:28px;font-weight:600;color:var(--gold);letter-spacing:.2px}
.nav-link{position:absolute;top:32px;font-size:14px;color:var(--ink);display:flex;align-items:center;gap:4px}
.btn-contact{position:absolute;left:1000px;top:24px;width:88px;height:33px;background:var(--navy);color:var(--white);font-size:14px;font-weight:500;display:flex;align-items:center;justify-content:center}

/* hero */
.hero{position:absolute;left:0;top:80px;width:1200px;height:534px;background:linear-gradient(160deg,#2f4a3d 0%,#1f3a4a 40%,#2d4e3a 70%,#1a2f3c 100%)}
.hero-title{position:absolute;left:0;width:1200px;top:186px;text-align:center;font-family:"Montserrat",Arial,sans-serif;font-weight:800;font-size:76px;color:var(--white);letter-spacing:1px;line-height:1}
.hero-sub{position:absolute;left:0;width:1200px;top:268px;text-align:center;font-size:20px;color:var(--white)}
.hero-dots{position:absolute;left:539px;top:313px;display:flex;gap:18px}
.hero-dots span{width:10px;height:10px;border-radius:50%;background:var(--white)}
.hero-dots span.on{background:var(--gold)}
.hero-rule{position:absolute;left:0;top:396px;width:1200px;height:1px;background:rgba(255,255,255,.7)}
.listing-strip{position:absolute;left:0;top:397px;width:1200px;height:137px;background:rgba(8,22,34,.55)}
.listing-strip .lit{position:absolute;left:0;top:0;width:316px;height:137px;background:rgba(40,90,130,.6)}
.strip-item{position:absolute;top:30px;color:var(--white)}
.strip-item h4{font-size:15px;font-weight:700;margin-bottom:12px}
.strip-item p{font-size:13.5px;line-height:17px;letter-spacing:.3px}

/* intro */
.intro{position:absolute;left:150px;top:712px;width:900px;text-align:center}
.intro h2{font-size:20px;font-weight:600;line-height:26.5px;color:var(--navy);white-space:nowrap}
.intro p{margin-top:22px;font-size:13px;line-height:21px;color:var(--ink);white-space:nowrap}

/* properties */
.glance-band{position:absolute;left:0;top:963px;width:1200px;height:490px;background:linear-gradient(180deg,#fbc862 0%,#fcc65a 60%,#f9be4f 100%)}
.glance-title{position:absolute;left:0;width:1200px;top:1026px;text-align:center;font-size:26px;font-weight:700;color:var(--navy);letter-spacing:.3px}
.tab{position:absolute;top:1119px;font-size:14px;color:var(--navy);transform:translateX(-50%);letter-spacing:.3px}
.tab.active{color:var(--white)}
.tab-line{position:absolute;left:305px;top:1143px;width:87px;height:3px;background:var(--white)}
.card{position:absolute;background:var(--white);border-left:1px solid var(--line);border-right:1px solid var(--line)}
.card-photo{width:100%}
.card-body{position:absolute;left:24px;right:24px}
.card h3{font-size:15px;font-weight:700;color:var(--navy)}
.card .addr{font-size:13.5px;color:var(--muted);line-height:17px;margin-top:6px;letter-spacing:.3px;width:190px}
.card-actions{position:absolute;right:0;top:0;display:flex;gap:10px}
.features{display:flex;gap:20px;align-items:center;font-size:13px;color:var(--muted)}
.features span{display:flex;align-items:center;gap:8px}
.price{font-size:20px;color:var(--ink)}
.more{font-size:13.5px;font-weight:600;color:var(--ink)}
.auction{font-size:15px;font-weight:700;color:var(--navy)}
.inspect-label{font-size:14px;font-weight:600;color:var(--muted)}
.inspect-date{font-size:13.5px;color:var(--muted);letter-spacing:.3px}
.btn-search{position:absolute;left:480px;top:1862px;width:241px;height:49px;background:var(--navy);color:var(--white);font-size:15.5px;font-weight:500;display:flex;align-items:center;justify-content:center}
.divider{position:absolute;left:117px;top:1949px;width:963px;height:1px;background:var(--line)}

/* blog */
.blog{position:absolute;left:105px;top:1986px;width:991px;height:450px;background:var(--navy)}
.blog-title{position:absolute;left:78px;top:66px;font-size:33px;font-weight:700;color:var(--white);letter-spacing:.3px}
.blog-title em{font-style:normal;color:var(--gold)}
.blog-dots{position:absolute;left:843px;top:76px;display:flex;gap:9px}
.blog-dots span{width:11px;height:11px;border-radius:50%;border:1.5px solid var(--white)}
.blog-dots span.on{background:var(--gold);border-color:var(--gold)}
.kicker{position:absolute;left:80px;top:180px;font-size:13px;font-weight:500;color:var(--white);letter-spacing:1.5px}
.feature-head{position:absolute;left:80px;top:212px;width:420px;font-size:26px;font-weight:600;line-height:32px;color:var(--white);white-space:nowrap}
.blog-vline{position:absolute;left:506px;top:156px;width:1px;height:218px;background:var(--gold)}
.insight-head{position:absolute;left:553px;top:178px;font-size:25px;font-weight:600;color:var(--white)}
.insight-rule{position:absolute;left:553px;top:256px;width:364px;height:1px;background:var(--gold)}
.topic-label{position:absolute;left:553px;top:284px;font-size:12.5px;font-weight:700;color:var(--white);letter-spacing:.3px}
.topic-link{position:absolute;left:553px;font-size:14px;color:var(--gold)}

/* testimonial */
.testimonial-title{position:absolute;left:0;width:1200px;top:2540px;text-align:center;font-size:21px;font-weight:600;color:var(--navy);letter-spacing:.3px}
.quote-mark{position:absolute;font-family:"Montserrat",Arial,sans-serif;font-size:72px;font-weight:800;color:var(--gold);line-height:1}
.quote-text{position:absolute;left:200px;top:2606px;width:822px;text-align:center;font-size:13.6px;font-style:italic;line-height:24.5px;color:var(--ink);white-space:nowrap}
.quote-name{position:absolute;left:0;width:1217px;top:2696px;text-align:center;font-size:16px;color:var(--ink)}

/* footer */
.site-footer{position:absolute;left:0;top:2758px;width:1200px;height:326px;background:var(--navy)}
.foot-col{position:absolute;top:40px;color:var(--white);font-size:14px}
.foot-col a{display:block;color:var(--white);text-decoration:none;line-height:16px;margin-bottom:10.5px}
.foot-col h5{font-size:15px;font-weight:600;color:var(--gold);margin-bottom:8px}
.foot-col p{line-height:26px}
.foot-rule{position:absolute;left:125px;top:266px;width:948px;height:1px;background:rgba(255,255,255,.35)}
.socials{position:absolute;left:936px;top:283px;display:flex;gap:14px}
.socials span{width:22px;height:22px;border-radius:4px;background:var(--white)}
</style>
</head>
<body>

<header class="site-header">
  <div class="brand"><span class="brand-mark"></span><span class="brand-name">Verindale</span></div>
  <span class="nav-link" style="left:332px">About</span>
  <span class="nav-link" style="left:398px">Leasing <svg width="12" height="8" viewBox="0 0 12 8"><path d="M1 1l5 5 5-5" fill="none" stroke="#1a2433" stroke-width="1.6"/></svg></span>
  <span class="nav-link" style="left:493px">Buy</span>
  <span class="nav-link" style="left:545px">Sell <svg width="12" height="8" viewBox="0 0 12 8"><path d="M1 1l5 5 5-5" fill="none" stroke="#1a2433" stroke-width="1.6"/></svg></span>
  <span class="nav-link" style="left:848px">Our Team</span>
  <span class="nav-link" style="left:941px">Blog</span>
  <span class="btn-contact">Contact</span>
</header>

<section class="hero" role="img" aria-label="Apartment building facade with balconies covered in hanging greenery">
  <div class="hero-title">VERINDALE</div>
  <div class="hero-sub">Spanish for “the home.”</div>
  <div class="hero-dots"><span class="on"></span><span></span><span></span><span></span><span></span></div>
  <div class="hero-rule"></div>
  <div class="listing-strip">
    <div class="lit"></div>
    <div class="strip-item" style="left:104px"><h4>GUNGAHLIN</h4><p>Level 5/18 Marlow<br>Crescent<br>Gungahlin.</p></div>
    <div class="strip-item" style="left:369px"><h4>BELCONNEN</h4><p>2002/44 Ridgeline<br>Way<br>Belconnen.</p></div>
    <div class="strip-item" style="left:634px"><h4>BELCONNEN</h4><p>172/9 Banksia Street<br>Belconnen</p></div>
    <div class="strip-item" style="left:928px"><h4>GUNGAHLIN</h4><p>Level 5/18 Marlow<br>Crescent<br>Gungahlin.</p></div>
  </div>
</section>

<section class="intro">
  <h2>Verindale in Spanish means “the home, the house”, buying a property is<br>one of the most expensive expenses and important assets for people.<br>Verindale is a real estate company located in Gungahlin, Canberra.</h2>
  <p>Being a portfolio sales agent and property manager, coupled with our high–profile international real estate<br>experience, Verindale is considered a market leader on the cutting edge with deep industry knowledge, ranging from<br>landlord–tenant relationships, residential purchases.</p>
</section>

<div class="glance-band" role="img" aria-label="Warm yellow tinted backdrop of a house roof and palm leaves"></div>
<h2 class="glance-title">PROPERTIES AT A GLANCE</h2>
<span class="tab active" style="left:347px">For Sale</span>
<span class="tab" style="left:481px">For Lease</span>
<span class="tab" style="left:627px">Open Times</span>
<span class="tab" style="left:752px">Sold</span>
<span class="tab" style="left:862px">Leased</span>
<div class="tab-line"></div>

<svg width="0" height="0" style="position:absolute">
  <defs>
    <symbol id="i-bed" viewBox="0 0 30 18"><path d="M2 16V3h26v13M2 11h26M6 11V7h8v4M16 11V7h8v4M1 16h28" fill="none" stroke="#0f2a44" stroke-width="1.4"/></symbol>
    <symbol id="i-bath" viewBox="0 0 26 22"><path d="M5 10V3a2 2 0 0 1 4 0M2 10h22v4a6 6 0 0 1-6 6H8a6 6 0 0 1-6-6zM6 20l-1 2M20 20l1 2" fill="none" stroke="#0f2a44" stroke-width="1.4"/></symbol>
    <symbol id="i-car" viewBox="0 0 40 16"><path d="M2 12V9l4-1 6-5h14l7 5 5 1v3h-3M9 12h20" fill="none" stroke="#0f2a44" stroke-width="1.4"/><circle cx="12" cy="12" r="2.5" fill="none" stroke="#0f2a44" stroke-width="1.4"/><circle cx="31" cy="12" r="2.5" fill="none" stroke="#0f2a44" stroke-width="1.4"/></symbol>
    <symbol id="i-mail" viewBox="0 0 12 10"><rect x="1" y="1" width="10" height="8" fill="none" stroke="#0f2a44" stroke-width="1.1"/><path d="M1 1l5 4 5-4" fill="none" stroke="#0f2a44" stroke-width="1.1"/></symbol>
    <symbol id="i-mark" viewBox="0 0 10 12"><path d="M1 0h8v12L5 9l-4 3z" fill="#0f2a44"/></symbol>
  </defs>
</svg>

<article class="card" style="left:102px;top:1182px;width:311px;height:598px">
  <div class="card-photo" style="height:337px;background:linear-gradient(180deg,#b9cde0 0%,#e6ecef 45%,#8a9a86 80%,#5c6a5a 100%)" role="img" aria-label="High-rise apartment tower above a suburban car park"></div>
  <div class="card-body" style="top:384px">
    <h3>BELCONNEN</h3>
    <div class="card-actions"><svg width="12" height="10"><use href="#i-mail"/></svg><svg width="10" height="12"><use href="#i-mark"/></svg></div>
    <p class="addr">2002/44 Ridgeline Way Belconnen</p>
    <div class="features" style="margin-top:22px"><span><svg width="30" height="18"><use href="#i-bed"/></svg>3</span><span><svg width="26" height="22"><use href="#i-bath"/></svg>2</span><span><svg width="40" height="16"><use href="#i-car"/></svg>2</span></div>
    <p class="price" style="margin-top:20px">$500,000+</p>
    <p class="more" style="margin-top:26px">Get more info</p>
  </div>
</article>

<article class="card" style="left:422px;top:1168px;width:350px;height:677px">
  <div class="card-photo" style="height:373px;background:linear-gradient(90deg,#8c9896 0%,#6f8aa8 40%,#3f66b0 60%,#a9bfd0 100%)" role="img" aria-label="Rooftop infinity pool with blue tiles beside an apartment tower"></div>
  <div class="card-body" style="top:418px">
    <h3>GUNGAHLIN</h3>
    <div class="card-actions"><svg width="12" height="10"><use href="#i-mail"/></svg><svg width="10" height="12"><use href="#i-mark"/></svg></div>
    <p class="addr">Level 5/18 Marlow Crescent Gungahlin</p>
    <div class="features" style="margin-top:22px"><span><svg width="30" height="18"><use href="#i-bed"/></svg>2</span><span><svg width="26" height="22"><use href="#i-bath"/></svg>2</span><span><svg width="40" height="16"><use href="#i-car"/></svg>1</span></div>
    <p class="auction" style="margin-top:26px">FORTHCOMING AUCTION</p>
    <p class="inspect-label" style="margin-top:10px">Next Inspection:</p>
    <p class="inspect-date" style="margin-top:6px">Sat 28th May 11:40 AM - 12:00 PM</p>
    <p class="more" style="margin-top:32px">Get more info</p>
  </div>
</article>

<article class="card" style="left:780px;top:1182px;width:311px;height:598px">
  <div class="card-photo" style="height:337px;background:linear-gradient(180deg,#dfe8ea 0%,#9fb3a8 40%,#2f4fc9 70%,#6a9a4a 100%)" role="img" aria-label="Outdoor swimming pool with shade sails, timber benches and lawn"></div>
  <div class="card-body" style="top:384px">
    <h3>BELCONNEN</h3>
    <div class="card-actions"><svg width="12" height="10"><use href="#i-mail"/></svg><svg width="10" height="12"><use href="#i-mark"/></svg></div>
    <p class="addr">172/9 Banksia Street Belconnen</p>
    <div class="features" style="margin-top:22px"><span><svg width="30" height="18"><use href="#i-bed"/></svg>1</span><span><svg width="26" height="22"><use href="#i-bath"/></svg>1</span><span><svg width="40" height="16"><use href="#i-car"/></svg>1</span></div>
    <p class="price" style="margin-top:20px">$500,000+</p>
    <p class="more" style="margin-top:26px">Get more info</p>
  </div>
</article>

<span class="btn-search">Search More Properties</span>
<div class="divider"></div>

<section class="blog">
  <h2 class="blog-title"><em>BLOGS</em> &amp; INSIGHTS</h2>
  <div class="blog-dots"><span class="on"></span><span></span><span></span></div>
  <p class="kicker">SPOTLIGHT ON OUR VALUES</p>
  <h3 class="feature-head">Harrowgate Capital LLC,<br>Among World's Most Admired<br>Companies</h3>
  <div class="blog-vline"></div>
  <h3 class="insight-head">Insights into the Future Trends.</h3>
  <div class="insight-rule"></div>
  <p class="topic-label">MORE ON THIS TOPIC</p>
  <p class="topic-link" style="top:316px">Building a Sustainable Future ⊠</p>
  <p class="topic-link" style="top:349px">Excellence, Integrity,</p>
</section>

<h2 class="testimonial-title">WHAT OUR CLIENT’S SAY ABOUT US.</h2>
<span class="quote-mark" style="left:190px;top:2590px">“</span>
<span class="quote-mark" style="left:936px;top:2658px">”</span>
<p class="quote-text">Lorem ipsum dolor sit amet, consectetur adipisicing elit, sed do eiusmod tempor incididunt ut labore et dolore magna<br>aliqua. Ut enim ad minim veniam, quis nostrud exercitation ullamco laboris nisi ut aliquip ex ea commodo consequat.<br>Duis aute irure dolor in reprehenderit in voluptate velit esse cillum dolore eu fugiat nulla pariatur.</p>
<p class="quote-name">Mei Lin</p>

<footer class="site-footer">
  <nav class="foot-col" style="left:183px"><a>Home</a><a>About</a><a>Leasing</a><a>Buy</a><a>Sell</a><a>Our Team</a></nav>
  <nav class="foot-col" style="left:328px"><a>Contact Us</a><a>Privacy</a><a>Complaint Handling &amp;<br>Dispute Resolution</a><a>Due Diligence Checklist</a></nav>
  <div class="foot-col" style="left:563px">
    <h5>Phone</h5>
    <p>P: (+ 02 - 6100 - 4821)<br>F: (+ 02 - 6100 - 4822)</p>
    <h5 style="margin-top:30px">Address</h5>
    <p>432/7 Marlow Crescent,<br>Gungahlin, ACT, 29123.</p>
  </div>
  <div class="foot-col" style="left:831px">
    <h5>Trading Hours</h5>
    <p>Mon-Fri / 8:30 AM - 5:00 PM.</p>
    <p style="margin-top:26px">Weekend – Closed<br>Public holiday – Closed</p>
    <p style="margin-top:36px">After hour by appointment.</p>
  </div>
  <div class="foot-rule"></div>
  <div class="socials"><span></span><span></span><span></span><span></span></div>
</footer>

</body>
</html>
```